LPC Brochure

A Brochure based on my website
www.lumenpartnerscircle.org that was made on draft meadow

Reason: Due to the Holiday here in the states and to give the new designers a little more time I would like to extend the date. I will also be out of town for a few days. Thank you.

```html
<!DOCTYPE html>
<html lang="en">
<head>
<meta charset="utf-8">
<title>Lumen Partners Circle Brochure</title>
<link rel="stylesheet" href="https://fonts.googleapis.com/css2?family=Oswald:wght@400;500;600&family=Open+Sans:wght@400;600;700&display=swap">
<style>
  :root {
    --navy: #0c3f5f;
    --navy-deep: #0a3552;
    --crimson: #8b1a1c;
    --cream: #fdf9f3;
    --ink: #333333;
    --white: #ffffff;
    --chirp-blue: #2aa3d8;
    --tack-red: #c8232c;
    --friend-blue: #3b5998;
    --kin-orange: #dc4a38;
  }
  html, body {
    margin: 0;
    padding: 0;
    width: 1200px;
    height: 927px;
    overflow: hidden;
    background: var(--white);
  }
  .brochure {
    position: relative;
    width: 1200px;
    height: 927px;
    overflow: hidden;
    font-family: "Open Sans", Arial, sans-serif;
    color: var(--ink);
  }
  .inside-top { position: absolute; left: 0; top: 0; width: 800px; height: 552px; background: var(--cream); }
  .inside-bottom { position: absolute; left: 0; top: 552px; width: 800px; height: 375px; background: var(--navy); }
  .cover-top { position: absolute; left: 800px; top: 0; width: 400px; height: 465px; background: var(--navy); }
  .cover-bottom { position: absolute; left: 800px; top: 465px; width: 400px; height: 462px; background: var(--crimson); }
  .art { position: absolute; left: 0; top: 0; }

  .luncheon { position: absolute; left: 34px; top: 36px; width: 350px; font-size: 14px; line-height: 18px; }
  .luncheon h2 {
    margin: 0 0 10px;
    font-family: "Oswald", "Arial Narrow", sans-serif;
    font-weight: 500;
    font-size: 17px;
    letter-spacing: 0.2px;
    color: var(--ink);
  }
  .luncheon p { margin: 0 0 18px; }
  .brand-inline { color: var(--crimson); font-weight: 600; }

  .details { position: absolute; left: 436px; top: 40px; width: 335px; margin: 0; padding: 0; list-style: none; font-size: 14px; line-height: 18px; }
  .details li { position: relative; padding-left: 25px; margin-bottom: 9px; }
  .details li::before { content: "•"; position: absolute; left: 0; top: 0; }
  .details b { font-weight: 700; }

  .social { position: absolute; left: 66px; top: 760px; display: flex; gap: 26px; }
  .social span {
    width: 52px; height: 52px;
    display: flex; align-items: center; justify-content: center;
    font-size: 9px; font-weight: 600; color: var(--white);
  }
  .social .murmur { background: var(--chirp-blue); }
  .social .tackboard { background: var(--tack-red); }
  .social .friendly { background: var(--friend-blue); }
  .social .kinship { background: var(--kin-orange); }

  .contact { position: absolute; left: 420px; top: 737px; width: 380px; text-align: center; color: var(--white); }
  .contact h3 { margin: 0 0 9px; font-family: "Oswald", "Arial Narrow", sans-serif; font-weight: 500; font-size: 17px; }
  .contact .moderator { font-size: 15px; letter-spacing: 0.3px; margin: 0 0 3px; }
  .contact .line { font-size: 11.5px; line-height: 18px; margin: 0; letter-spacing: 0.2px; }

  .title {
    position: absolute; left: 800px; top: 62px; width: 400px;
    text-align: center; color: var(--white);
    font-family: "Oswald", "Arial Narrow", sans-serif; font-weight: 400;
    font-size: 40px; line-height: 44px; margin: 0;
  }
  .join {
    position: absolute; left: 800px; top: 726px; width: 400px;
    text-align: center; color: var(--white); margin: 0;
    font-family: "Oswald", "Arial Narrow", sans-serif; font-weight: 500;
    font-size: 35px; line-height: 37px; letter-spacing: 0.2px;
  }
  .web { position: absolute; left: 800px; top: 875px; width: 400px; text-align: center; color: var(--white); font-size: 13px; font-weight: 700; letter-spacing: 0.3px; margin: 0; }
</style>
</head>
<body>
<main class="brochure">
  <div class="inside-top"></div>
  <div class="inside-bottom"></div>
  <div class="cover-top"></div>
  <div class="cover-bottom"></div>

  <svg class="art" width="1200" height="927" viewBox="0 0 1200 927" aria-hidden="false">
    <defs>
      <symbol id="star" viewBox="-1 -1 2 2">
        <polygon fill="#ffffff" points="0,-1 0.2245,-0.309 0.951,-0.309 0.363,0.118 0.588,0.809 0,0.382 -0.588,0.809 -0.363,0.118 -0.951,-0.309 -0.2245,-0.309"/>
      </symbol>
      <linearGradient id="tone-dark" x1="0" y1="0" x2="1" y2="1"><stop offset="0" stop-color="#5a463c"/><stop offset="1" stop-color="#2a211d"/></linearGradient>
      <linearGradient id="tone-light" x1="0" y1="0" x2="1" y2="1"><stop offset="0" stop-color="#e6e8ea"/><stop offset="1" stop-color="#a9b4c2"/></linearGradient>
      <linearGradient id="tone-warm" x1="0" y1="0" x2="1" y2="1"><stop offset="0" stop-color="#b57d6a"/><stop offset="1" stop-color="#3d2a26"/></linearGradient>
      <linearGradient id="tone-room" x1="0" y1="0" x2="1" y2="1"><stop offset="0" stop-color="#d9cfbf"/><stop offset="1" stop-color="#5f6b4c"/></linearGradient>
      <linearGradient id="tone-office" x1="0" y1="0" x2="1" y2="1"><stop offset="0" stop-color="#a46a4c"/><stop offset="1" stop-color="#eef0f2"/></linearGradient>
      <linearGradient id="tone-team" x1="0" y1="0" x2="1" y2="1"><stop offset="0" stop-color="#b9c6d2"/><stop offset="1" stop-color="#c9b79c"/></linearGradient>
    </defs>

    <!-- star rows -->
    <g class="stars-large">
      <use href="#star" x="824" y="24" width="22" height="22"/><use href="#star" x="857" y="24" width="22" height="22"/>
      <use href="#star" x="890" y="24" width="22" height="22"/><use href="#star" x="923" y="24" width="22" height="22"/>
      <use href="#star" x="955" y="24" width="22" height="22"/><use href="#star" x="988" y="24" width="22" height="22"/>
      <use href="#star" x="1021" y="24" width="22" height="22"/><use href="#star" x="1054" y="24" width="22" height="22"/>
      <use href="#star" x="1087" y="24" width="22" height="22"/><use href="#star" x="1119" y="24" width="22" height="22"/>
      <use href="#star" x="1152" y="24" width="22" height="22"/>
    </g>
    <g class="stars-small">
      <use href="#star" x="905" y="205" width="11" height="11"/><use href="#star" x="922" y="205" width="11" height="11"/>
      <use href="#star" x="939" y="205" width="11" height="11"/><use href="#star" x="955" y="205" width="11" height="11"/>
      <use href="#star" x="972" y="205" width="11" height="11"/><use href="#star" x="989" y="205" width="11" height="11"/>
      <use href="#star" x="1006" y="205" width="11" height="11"/><use href="#star" x="1023" y="205" width="11" height="11"/>
      <use href="#star" x="1039" y="205" width="11" height="11"/><use href="#star" x="1056" y="205" width="11" height="11"/>
      <use href="#star" x="1073" y="205" width="11" height="11"/>
    </g>

    <!-- cover chevron -->
    <polyline points="1190,318 1046,462 1170,612" fill="none" stroke="#ffffff" stroke-width="16"/>

    <!-- inside diamonds -->
    <g role="img" aria-label="Photo: clasped hands in a group session">
      <polygon points="245,225 350,330 245,435 140,330" fill="var(--navy)"/>
      <polygon points="245,237 338,330 245,423 152,330" fill="url(#tone-dark)"/>
    </g>
    <g role="img" aria-label="Photo: woman speaking and gesturing">
      <polygon points="128,340 250,462 128,584 6,462" fill="var(--crimson)"/>
      <polygon points="128,352 238,462 128,572 18,462" fill="url(#tone-light)"/>
    </g>
    <g role="img" aria-label="Photo: three colleagues in business attire">
      <polygon points="258,475 368,585 258,695 148,585" fill="#ffffff"/>
      <polygon points="258,485 358,585 258,685 158,585" fill="url(#tone-light)"/>
    </g>
    <g role="img" aria-label="Photo: close-up of hands held in support">
      <polygon points="455,252 665,462 455,672 245,462" fill="var(--crimson)"/>
      <polygon points="455,266 651,462 455,658 259,462" fill="url(#tone-warm)"/>
    </g>
    <g role="img" aria-label="Photo: older man talking in a meeting room">
      <polygon points="645,342 765,462 645,582 525,462" fill="var(--crimson)"/>
      <polygon points="645,354 753,462 645,570 537,462" fill="url(#tone-room)"/>
    </g>

    <!-- cover diamonds -->
    <g role="img" aria-label="Photo: smiling man at a business meeting">
      <polygon points="1015,222 1133,340 1015,458 897,340" fill="var(--crimson)"/>
      <polygon points="1015,234 1121,340 1015,446 909,340" fill="url(#tone-office)"/>
    </g>
    <g role="img" aria-label="Photo: smiling woman at a conference table">
      <polygon points="905,344 1023,462 905,580 787,462" fill="#ffffff"/>
      <polygon points="905,354 1013,462 905,570 797,462" fill="url(#tone-office)"/>
    </g>
    <g role="img" aria-label="Photo: team of professionals posing together">
      <polygon points="1015,465 1135,585 1015,705 895,585" fill="var(--navy-deep)"/>
      <polygon points="1015,475 1125,585 1015,695 905,585" fill="url(#tone-team)"/>
    </g>
  </svg>

  <section class="luncheon">
    <h2>MONTHLY NETWORKING LUNCHEON</h2>
    <p>The <span class="brand-inline">Lumen Partners Circle</span> meets for lunch the first Friday of every month. RSVPs Only. No Walk-ins. Space is limited to the first 22 to reserve space.</p>
    <p>Please bring business cards and brochures to share.</p>
    <p>Special Feature: Each month there will be a different sponsor for appetizers and chocolate-covered strawberries for dessert.</p>
  </section>

  <ul class="details">
    <li><b>What:</b> A networking luncheon to meet new colleagues and schmooz with old friends.</li>
    <li><b>When:</b> The First Friday of Every Month noon – 1:30 p.m.</li>
    <li><b>Where:</b> The Harbor Table, 4120 Linden Avenue, Maple Heights, MD 20900 (Free parking with validation at Linden Square.)</li>
    <li><b>Cost:</b> $25 per person (cash please). All-inclusive of beverage, a great meal and gratuity.</li>
  </ul>

  <nav class="social" aria-label="Social channels">
    <span class="murmur">Murmur</span>
    <span class="tackboard">Tackboard</span>
    <span class="friendly">Friendly</span>
    <span class="kinship">Kinship</span>
  </nav>

  <section class="contact">
    <h3>CONTACT TO JOIN</h3>
    <p class="moderator">DANA WHITFIELD, LICSW, CASAC– MODERATOR</p>
    <p class="line">2200 ALDER ST., NW #310 WASHINGTON, DC 20008</p>
    <p class="line">(202)555-0148</p>
    <p class="line">CIRCLE@LUMENPARTNERSMAIL.ORG</p>
  </section>

  <h1 class="title">Lumen<br>Partners<br>Circle</h1>
  <h2 class="join">JOIN 500 MENTAL HEALTH,<br>SUBSTANCE ABUSE AND<br>ADDICTION PROFESSIONALS</h2>
  <p class="web">WWW.LUMENPARTNERSCIRCLE.ORG</p>
</main>
</body>
</html>
```